IT-support company web-site design

We need to re-design out site for existing clients and for the future promotions. Site needs to be attractive with intuitive interface. We need to keep our logo and colors but any reshuffles can be made. I provide the working site and re-made version, which we do nt like. It has to be more bright and clear. All the blocks have to be divided and look like logic and structured. PLease find the addresses to work with below.
The "real" one https://plorim.com
The version http://dostuly.net/Plorim/
If you have any с

Industry/Entity Type

It Company

Number of Pages Required

5+ page

Font styles to use
Sans Serif

Colors
9bcb3c

Requirements
Must have
• Our LOGO and our colors (green palette). We d like to make our services blocks as the main things. We need to have our images and slogans as there are extremely important advantages of our company.
Nice to have
• Original and modern view of the site.
Should not have
• unpredictable and @surprising@, hard- definable buttons and ways

```html
<!DOCTYPE html>
<html lang="en">
<head>
<meta charset="utf-8">
<title>Plorim – IT made simple and secure</title>
<link href="https://fonts.googleapis.com/css2?family=Raleway:wght@300;400;500;600&family=Montserrat:wght@400;500;600;700&display=swap" rel="stylesheet">
<style>
:root{
  --green:#9bcb3c;
  --green-dark:#7fb52a;
  --mint:#6fd3a0;
  --mint-light:#a5e0a6;
  --ink:#3d3d3d;
  --muted:#6a6a6a;
  --faint:#b5b5b5;
  --footer:#8f8f8f;
  --white:#ffffff;
}
*{margin:0;padding:0;box-sizing:border-box}
html,body{width:843px;height:1200px;overflow:hidden;background:var(--white)}
body{position:relative;font-family:'Montserrat',sans-serif;color:var(--ink)}
h1,h2,h3,h4{font-weight:400}
.abs{position:absolute}

/* header + hero */
.hero{left:0;top:0;width:843px;height:307px;background:linear-gradient(90deg,#f6f6f4 0%,#fbfbfa 45%,#f1f0ee 100%);overflow:hidden}
.hero-photo{right:90px;top:38px;width:290px;height:269px;background:linear-gradient(160deg,#efe2dc 0%,#e7d0c8 40%,#d9dde2 75%,#c9ced6 100%);border-radius:140px 140px 0 0;opacity:.9}
.hero-desk{left:248px;top:258px;width:520px;height:49px;background:linear-gradient(90deg,#dfe4ea,#eef0f3);}
.logo{display:flex;align-items:center;gap:6px;font-family:'Raleway',sans-serif;font-weight:400;font-size:18px;color:#555;letter-spacing:1px}
.logo-dot{width:12px;height:12px;border:1.5px solid var(--mint);border-radius:50%}
.header-logo{left:165px;top:13px}
.nav{left:299px;top:17px;display:flex;gap:17px;font-size:6.4px;color:#555;font-weight:500}
.nav .active{color:var(--green)}
.btn{background:var(--green);color:#fff;font-weight:700;text-transform:uppercase;border-radius:12px;display:flex;align-items:center;justify-content:center}
.login{left:608px;top:12px;width:70px;height:20px;font-size:5.4px}
.hero-title{left:171px;top:78px;font-family:'Raleway',sans-serif;font-weight:400;font-size:22px;color:#555}
.hero-title em{font-style:normal;color:var(--green)}
.hero-sub{left:171px;top:134px;font-family:'Montserrat',sans-serif;font-weight:600;font-size:15.5px;line-height:22px;color:#555}
.call{left:167px;top:217px;width:88px;height:20px;font-size:5.2px}

/* service tiles */
.tiles{left:164px;top:329px;display:flex;gap:18.5px}
.tile{width:88px;height:92px;background:linear-gradient(180deg,#8fe0a5,#6fcfa0);display:flex;flex-direction:column;align-items:center;justify-content:flex-end;padding-bottom:14px;color:#fff;font-size:6.2px;font-weight:600;text-align:center;line-height:8px}
.tile.active{background:var(--green);box-shadow:0 6px 12px rgba(0,0,0,.12)}
.tile svg{margin-bottom:10px}

/* intro */
.intro-title{left:164px;top:455px;font-family:'Raleway',sans-serif;font-weight:400;font-size:11px;line-height:11.5px;color:#333}
.intro-title em{font-style:normal;color:var(--green)}
.intro-text{left:164px;top:490px;width:260px;font-size:5.6px;line-height:11px;color:#666}
.intro-text p{margin-bottom:5px}
.checks{left:472px;top:455px;list-style:none;font-size:6.2px;color:#555}
.checks li{display:flex;align-items:center;gap:7px;height:16px}

/* stats band */
.band{left:0;top:570px;width:843px;height:350px;background:linear-gradient(100deg,#6fd3a0 0%,#8bdba6 50%,#a3e0a2 100%)}
.band-title{left:0;top:600px;width:843px;text-align:center;font-family:'Raleway',sans-serif;font-weight:400;font-size:16.5px;color:#fff}
.band-sub{left:0;top:626px;width:843px;text-align:center;font-size:6.2px;color:#eafaf0}
.stats{left:244px;top:652px;display:flex}
.stat{width:92px;text-align:center;color:#fff}
.stat b{display:block;font-family:'Raleway',sans-serif;font-weight:300;font-size:26px;height:36px}
.stat b small{font-size:13px}
.stat span{font-size:6px}
.card{top:723px;height:140px;background:#fff;box-shadow:0 3px 10px rgba(0,0,0,.06);text-align:center;font-style:italic;font-size:6.1px;line-height:11.5px;color:#555;padding:28px 26px 0}
.card h4{font-style:normal;font-weight:600;font-size:7.2px;color:#333;margin-bottom:2px}
.card .co{font-style:normal;font-size:5.4px;color:#bbb;margin-bottom:8px}
.card-main{left:208px;width:425px}
.card-left{left:-230px;width:425px;text-align:right}
.card-right{left:648px;width:425px;text-align:left}
.dots{left:409px;top:880px;display:flex;gap:5px}
.dots i{width:5px;height:5px;border:1px solid #fff;border-radius:50%}
.dots i.on{background:#fff}

/* partners */
.partners-title{left:0;top:942px;width:843px;text-align:center;font-family:'Raleway',sans-serif;font-weight:400;font-size:15px;color:#333}
.partners-sub{left:0;top:968px;width:843px;text-align:center;font-size:6.2px;line-height:8px;color:#777}
.partner-row{left:160px;top:1012px;display:flex;align-items:center;gap:47px}
.badge{height:28px;background:#e4e8e2;border-radius:3px}
.arrow{top:1025px}

/* footer */
.footer{left:0;top:1072px;width:843px;height:128px;background:var(--footer);color:#fff}
.footer .logo{color:#fff;position:absolute;left:165px;top:30px;font-size:13px}
.footer .logo-dot{border-color:#fff;width:10px;height:10px}
.social{left:165px;top:59px;display:flex;gap:13px}
.social i{width:6px;height:6px;border:1px solid #fff}
.copy{left:164px;top:80px;font-size:6px}
.fcol{font-size:6px;line-height:13px}
</style>
</head>
<body>

<div class="abs hero">
  <div class="abs hero-photo" role="img" aria-label="Photo of a support agent on the phone at a laptop"></div>
  <div class="abs hero-desk" role="img" aria-label="Office desk and chairs"></div>
</div>

<div class="abs logo header-logo"><span class="logo-dot"></span>PLORIM</div>
<nav class="abs nav">
  <span class="active">Plorim Difference</span><span>Services</span><span>Resources</span><span>Customer</span><span>Support</span><span>Contact Us</span>
</nav>
<div class="abs btn login">Customer Login</div>

<h1 class="abs hero-title">We make IT <em>simple</em> and <em>secure</em></h1>
<h2 class="abs hero-sub">LIVE LOCAL 24/7<br>HELP DESK AND TIER 3 SUPPORT</h2>
<div class="abs btn call">Call Now!</div>

<section class="abs tiles">
  <div class="tile">
    <svg width="26" height="26" viewBox="0 0 26 26" fill="none" stroke="#fff" stroke-width="1.2"><circle cx="15" cy="10" r="7"/><ellipse cx="15" cy="10" rx="3" ry="7"/><path d="M8 10h14M2 20h7l5 2 9-4"/></svg>
    Freedom from<br>IT Worries.
  </div>
  <div class="tile active">
    <svg width="26" height="26" viewBox="0 0 26 26" fill="none" stroke="#fff" stroke-width="1.2"><path d="M2 12a11 9 0 0 1 22 0z"/><path d="M13 12v6"/><circle cx="13" cy="20" r="4"/><path d="M13 18v4"/></svg>
    Eliminate<br>Unpredictable<br>IT Expenses.<br>Reduce IT Costs
  </div>
  <div class="tile">
    <svg width="26" height="26" viewBox="0 0 26 26" fill="none" stroke="#fff" stroke-width="1.6"><path d="M4 15a9 9 0 0 1 18 0"/><rect x="3" y="14" width="4" height="7" rx="1"/><rect x="19" y="14" width="4" height="7" rx="1"/></svg>
    Houston-based 24/7<br>Help Desk Support
  </div>
  <div class="tile">
    <svg width="26" height="26" viewBox="0 0 26 26" fill="none" stroke="#fff" stroke-width="1.2"><circle cx="9" cy="9" r="6" stroke-dasharray="2 1.5"/><circle cx="17" cy="17" r="6" stroke-dasharray="2 1.5"/><circle cx="9" cy="9" r="3"/><circle cx="17" cy="17" r="3"/></svg>
    Eliminate<br>Unpredictable<br>IT Expenses.<br>Reduce IT Costs
  </div>
  <div class="tile">
    <svg width="26" height="34" viewBox="0 0 26 34" fill="none" stroke="#fff" stroke-width="1.2"><circle cx="13" cy="6" r="5"/><path d="M3 28a10 10 0 0 1 20 0"/><circle cx="13" cy="24" r="5" stroke-dasharray="2 1.5"/><circle cx="13" cy="24" r="2"/></svg>
    Our Services
  </div>
</section>

<h3 class="abs intro-title">We Make Your Information Technology<br><em>SECURE</em> and <em>SIMPLE</em></h3>
<div class="abs intro-text">
  <p>Lorem ipsum dolor sit amet, consectetur adipisicing elit, sed do eiusmod tempor dunt ut labore et dolore magna aliqua.</p>
  <p>Ut enim ad minim veniam, quis nostrud exercitation ullamco laboris nisi ut aliquip ex ea commodo consequat. Duis aute irure dolor in reprehenderit.</p>
</div>
<ul class="abs checks">
  <li><svg width="7" height="6" viewBox="0 0 7 6"><path d="M1 3l2 2 3-4" stroke="#9bcb3c" stroke-width="1.5" fill="none"/></svg>Massa erat pretium arcu, nec eleifend.</li>
  <li><svg width="7" height="6" viewBox="0 0 7 6"><path d="M1 3l2 2 3-4" stroke="#9bcb3c" stroke-width="1.5" fill="none"/></svg>Nullam lorem enim, faucibus a turpis eu luctus.</li>
  <li><svg width="7" height="6" viewBox="0 0 7 6"><path d="M1 3l2 2 3-4" stroke="#9bcb3c" stroke-width="1.5" fill="none"/></svg>Aenean sit amet lobortis metus. In tempor dui et hendrerit.</li>
  <li><svg width="7" height="6" viewBox="0 0 7 6"><path d="M1 3l2 2 3-4" stroke="#9bcb3c" stroke-width="1.5" fill="none"/></svg>Nullam lorem enim, faucibus a turpis eu luctus.</li>
</ul>

<div class="abs band" role="img" aria-label="Soft green background with a faint office photo"></div>
<h2 class="abs band-title">Our success is measured by our client’s growth.</h2>
<p class="abs band-sub">Companies worldwide trust Plorim to help them maximize the value of IT and improve user efficiency and productivity.</p>
<div class="abs stats">
  <div class="stat"><b>35</b><span>Years of Experience</span></div>
  <div class="stat"><b>10<small>k</small></b><span>Happy Customers</span></div>
  <div class="stat"><b>99.9%</b><span>Uptime Guaranteed</span></div>
  <div class="stat"><b>100<small>%</small></b><span>Satisfied Customers</span></div>
</div>

<div class="abs card card-left">
  <h4>Lena Harvick, MD,PA</h4>
  <div class="co">Family Clinic</div>
  Staying up-to- date with ever-growing record keeping and patient care lets me focus on running my practice.
</div>
<div class="abs card card-main">
  <h4>Dana Welloway</h4>
  <div class="co">Brell, Oakes &amp; Tamsin, LLC</div>
  Through the variety of services offered and their knowledgeable, professional, and friendly staff, Plorim provides our company with a true partner for our IT needs. Plorim saves us time and money – top items on any business owner’s list. BOT has had a business relationship with Plorim since our firm had to temporarily relocate to Houston after Hurricane Katrina in 2005. Everyone at Plorim has always been quick to help and educate along the way so that we are not only getting a problem solved, we are helping each other out to continue to build an efficient partnership for both companies.
</div>
<div class="abs card card-right">
  <h4>Teodor Vaskel</h4>
  <div class="co">&nbsp;</div>
  I can’t imagine growing as rapidly as we have without the advantages over the competition, and I never worry about IT.
</div>
<div class="abs dots"><i></i><i class="on"></i><i></i></div>

<h2 class="abs partners-title">OUR PARTNERS Who’s using Plorim | Assist?</h2>
<p class="abs partners-sub">IT Technology will eventually deliver its greatest value to American business<br>when it becomes invisible to users, when it can be taken for granted.</p>
<svg class="abs arrow" style="left:76px" width="10" height="16" viewBox="0 0 10 16"><path d="M8 1L2 8l6 7" stroke="#9bcb3c" fill="none" stroke-width="1.2"/></svg>
<div class="abs partner-row">
  <div class="badge" style="width:46px;height:38px"></div>
  <div class="badge" style="width:70px"></div>
  <div class="badge" style="width:62px;height:14px"></div>
  <div class="badge" style="width:42px;height:18px"></div>
  <div class="badge" style="width:40px;height:24px"></div>
  <div class="badge" style="width:40px;height:22px"></div>
</div>
<svg class="abs arrow" style="left:757px" width="10" height="16" viewBox="0 0 10 16"><path d="M2 1l6 7-6 7" stroke="#9bcb3c" fill="none" stroke-width="1.2"/></svg>

<footer class="abs footer">
  <div class="logo"><span class="logo-dot"></span>PLORIM</div>
  <div class="abs social"><i></i><i></i><i></i><i></i></div>
  <div class="abs copy">Copyright 2017 Plorim | All Rights Reserved</div>
  <div class="abs fcol" style="left:340px;top:42px">Helpful Tips<br>FAQ’s<br>White Papers</div>
  <div class="abs fcol" style="left:427px;top:42px">Local PC Support<br>Helpdesk App<br>Live 24/7 Remote<br>PC Support</div>
  <div class="abs fcol" style="left:516px;top:40px">4820 Linden Creek Road,<br>Houston, TX 77031<br>Phone: (555) - 018 - 2746<br>Email: info@plorim.com</div>
</footer>

</body>
</html>
```